ベースの色はグリーンですが、その系統の配色か、必要に応じては青をいれてもらってもかまいません。コーポレートサイトのデザインですが、色々な方のパターンを見てみたいです。
採用も目的としているため比較的爽やかなイメージが良いかもしれません。
仕様書【ミライワークス用】.pdfと添付画像をもとにデザイン作成お願いします。

当選前提となった方は正式な社名及び連絡先をお伝えしますので修正対応をお願いします。
また希望の際は、当選後、中ページの制作及びコーディングも別途ご依頼可能です。
ページ数
1ページ
希望イメージ
シンプル 複雑
単色 カラフル
暗い 明るい
日常 高級
遊び心 厳粛
未来的 伝統的
女性的 男性的
希望する色
緑系、青系
納品ファイル
• 高解像度JPG (.jpg)
• フォトショップ形式 (.psd)
弊社で納品している運送系サイトを参考までに記載します。

https://www.harunomiya.co.jp/
https://www.mido-hakobi.co.jp/
https://www.tachibe-web.co.jp/
https://www.renkaru.net/
■ 選んだ理由

採用を意識したイメージと、全体のメリハリ感が非常にマッチしておりました。
ありがとうございます。

■ 提案者全員のお礼・コメント

たくさんのご提案ありがとうございます。
どれも非常にレベルが高く弊社デザイナー感でも意見が割れて迷いました。
またの機会がありましたらよろしくお願いいたします。

```html
<!DOCTYPE html>
<html lang="ja">
<head>
<meta charset="utf-8">
<title>株式会社〇〇運送</title>
<link href="https://fonts.googleapis.com/css2?family=Noto+Sans+JP:wght@400;500;700;900&family=Montserrat:wght@500;600;700&display=swap" rel="stylesheet">
<style>
:root{
  --green:#3aa63f;
  --green-dark:#2e8c34;
  --green-pale:#eaf6e6;
  --blue:#2f52a8;
  --ink:#333;
  --muted:#666;
  --white:#fff;
}
*{margin:0;padding:0;box-sizing:border-box}
html,body{width:1200px;height:3520px;overflow:hidden}
body{position:relative;background:var(--white);font-family:"Noto Sans JP",sans-serif;color:var(--ink)}
.abs{position:absolute}

/* header */
.site-header{left:0;top:0;width:1200px;height:88px;background:var(--white)}
.brand{left:20px;top:14px;font-size:34px;font-weight:900;color:var(--green);letter-spacing:1px}
.brand-sub{left:20px;top:62px;font-size:11px;color:var(--muted)}
.global-nav{left:326px;top:36px;display:flex;gap:30px;font-size:15px;font-weight:500}
.tel-button{left:1030px;top:0;width:170px;height:76px;background:var(--green);color:var(--white);display:flex;flex-direction:column;align-items:center;justify-content:center;font-family:"Montserrat",sans-serif;font-weight:600;font-size:16px;gap:4px}

/* hero */
.hero{left:0;top:88px;width:1200px;height:732px;background:linear-gradient(135deg,#d8e6d0 0%,#eef2f4 30%,#c9d4dc 60%,#9aa7b3 100%)}
.hero-catch{left:240px;top:285px;color:var(--white);text-shadow:0 2px 6px rgba(0,0,0,.3)}
.hero-catch .jp{font-size:26px;font-weight:500;margin-left:60px}
.hero-catch .en{font-family:"Montserrat",sans-serif;font-size:48px;font-weight:600;margin-top:6px;display:flex;align-items:center;gap:12px}
.hero-catch .en i{display:inline-block;width:22px;height:22px;background:var(--green)}
.hero-note{left:80px;top:575px;width:400px;height:150px;background:rgba(255,255,255,.85);padding:28px 30px;font-size:15px;line-height:1.9;color:var(--ink)}

/* certification */
.cert-glow{left:0;top:900px;width:1200px;height:300px;background:radial-gradient(ellipse at center,#f3f9e6 0%,rgba(255,255,255,0) 70%)}
.cert-badge{left:490px;top:838px;width:222px;height:230px;background:#3f6fc0;border:10px solid #8cc63f}
.cert-text{left:0;top:1170px;width:1200px;text-align:center;font-size:21px;line-height:2;color:var(--ink)}

/* business */
.biz-pale{left:0;top:1760px;width:600px;height:220px;background:var(--green-pale)}
.section-title{font-size:34px;font-weight:700;color:var(--green)}
.section-title::after{content:"";display:block;width:60px;height:4px;background:var(--green);margin-top:10px}
.biz-title{left:80px;top:1390px}
.biz-text{left:80px;top:1480px;width:480px;font-size:15px;line-height:1.85;color:var(--ink);word-break:break-all}
.more-btn{width:360px;height:62px;background:var(--green);color:var(--white);display:flex;align-items:center;justify-content:space-between;padding:0 32px;font-family:"Montserrat",sans-serif;font-size:15px;font-weight:500}
.biz-more{left:80px;top:1808px}
.biz-photo{left:610px;top:1400px;width:590px;height:360px;background:linear-gradient(120deg,#c8d4de 0%,#8b9fb8 40%,#3d5aa0 60%,#dfe6ec 100%)}

/* category banners */
.cat{top:2050px;width:400px;height:250px;display:flex;align-items:center;justify-content:center;color:var(--white);font-size:22px;font-weight:700;text-shadow:0 1px 4px rgba(0,0,0,.4)}
.cat-env{left:0;background:linear-gradient(135deg,#4f9a3c,#2d6a2a)}
.cat-vehicle{left:400px;background:linear-gradient(135deg,#b86a4a,#6e3a2c)}
.cat-company{left:800px;background:linear-gradient(135deg,#8fa9cf,#5f7fb5)}

/* recruit */
.recruit-band{left:0;top:2300px;width:1200px;height:480px;background:var(--green)}
.recruit-card{left:80px;top:2350px;width:1040px;height:380px;background:var(--white)}
.recruit-photo{left:100px;top:2390px;width:500px;height:340px;background:linear-gradient(160deg,#e9eef2 0%,#5d86c9 60%,#2f52a8 100%)}
.recruit-title{left:680px;top:2400px}
.recruit-text{left:680px;top:2490px;width:400px;font-size:15px;line-height:1.85}
.recruit-more{left:680px;top:2630px;width:310px}

/* contact */
.contact-title{left:0;top:2830px;width:1200px;text-align:center;font-size:34px;font-weight:700;color:var(--green)}
.contact-text{left:0;top:2905px;width:1200px;text-align:center;font-size:15px;line-height:1.9}
.contact-pale{left:0;top:3140px;width:1200px;height:180px;background:var(--green-pale)}
.contact-btn{top:3010px;width:510px;height:180px;color:var(--white);display:flex;flex-direction:column;align-items:center;justify-content:center;gap:16px;font-size:22px;font-weight:700}
.contact-phone{left:80px;background:var(--blue)}
.contact-mail{left:610px;background:var(--green)}

/* footer */
.footer-brand{left:80px;top:3360px;font-size:38px;font-weight:900;color:var(--green)}
.footer-address{left:420px;top:3368px;font-size:13px;line-height:1.8;color:var(--muted)}
.footer-nav{left:680px;top:3360px;display:grid;grid-template-columns:repeat(4,auto);gap:14px 40px;font-size:14px}
.copyright{left:0;top:3490px;width:1200px;height:30px;background:var(--green);color:var(--white);font-size:11px;display:flex;align-items:center;justify-content:center}
</style>
</head>
<body>

<header class="abs site-header">
  <div class="abs brand">株式会社〇〇運送</div>
  <div class="abs brand-sub">営業時間：9:00〜17:00 / 定休日：土・日・祝日</div>
  <nav class="abs global-nav">
    <span>ホーム</span><span>事業案内</span><span>環境品質方針</span><span>車両案内</span><span>採用情報</span><span>会社案内</span><span>お問い合わせ</span>
  </nav>
  <div class="abs tel-button">
    <svg width="26" height="26" viewBox="0 0 24 24" fill="#fff"><path d="M6.6 10.8a15 15 0 0 0 6.6 6.6l2.2-2.2a1 1 0 0 1 1-.25 11.4 11.4 0 0 0 3.6.57 1 1 0 0 1 1 1V20a1 1 0 0 1-1 1A17 17 0 0 1 3 4a1 1 0 0 1 1-1h3.5a1 1 0 0 1 1 1c0 1.25.2 2.45.57 3.57a1 1 0 0 1-.25 1z"/></svg>
    <span>000-000-0000</span>
  </div>
</header>

<section class="abs hero" role="img" aria-label="青空の下に並ぶトラックの写真"></section>
<div class="abs hero-catch">
  <div class="jp">安全・安心・信頼される企業として</div>
  <div class="en"><i></i>Reliability &amp; safety &amp; reliability</div>
</div>
<div class="abs hero-note">
  長年の経験と実績を活かし、<br>お客様の様々なニーズにお応えできるよう、<br>真心込めたサービスを提供してまいります。
</div>

<div class="abs cert-glow" role="img" aria-label="淡い緑の木漏れ日の背景"></div>
<div class="abs cert-badge" role="img" aria-label="安全認定の証"></div>
<p class="abs cert-text">株式会社〇〇運送は全国輸送安全協会が推進する「輸送安全優良事業者」の認定制度において、<br>安全性の高いトラック運送事業者として認定され、安全認定マークを取得いたしました。</p>

<div class="abs biz-pale"></div>
<h2 class="abs section-title biz-title">事業内容</h2>
<p class="abs biz-text">グリーンテキストグリーンテキストグリーンテキストグリーンテキストグリーンテキストグリーンテキストグリーンテキストグリーンテキストグリーンテキストグリーンテキストグリーンテキストグリーンテキストグリーンテキストグリーンテキストグリーンテキストグリーンテキストグリーンテキストグリーンテキストグリーンテキストグリーンテキストグリーンテキストグリーンテキストグリーンテキストグリーンテキストグリーンテキストグリーンテキストグリーンテキストグリーンテキストグリーンテキスト</p>
<div class="abs more-btn biz-more"><span>more</span><span>→</span></div>
<div class="abs biz-photo" role="img" aria-label="車庫に並ぶトラックの写真"></div>

<div class="abs cat cat-env" role="img" aria-label="緑の自然の写真">環境・品質方針</div>
<div class="abs cat cat-vehicle" role="img" aria-label="トラック車両の写真">車両案内</div>
<div class="abs cat cat-company" role="img" aria-label="会社の建物の写真">会社案内</div>

<div class="abs recruit-band"></div>
<div class="abs recruit-card"></div>
<div class="abs recruit-photo" role="img" aria-label="作業着姿の社員二人の写真"></div>
<h2 class="abs section-title recruit-title">採用情報</h2>
<p class="abs recruit-text">〇〇運送では、一緒に働く仲間を募集しています。弊社の業務にご興味をお持ちの方は、ぜひお気軽にお問い合わせください。</p>
<div class="abs more-btn recruit-more"><span>more</span><span>→</span></div>

<h2 class="abs contact-title">お問い合わせ</h2>
<p class="abs contact-text">当社へのお問い合わせやご質問・ご相談・採用をご希望される方は<br>お電話またはメールフォームよりお問い合わせください。</p>
<div class="abs contact-pale"></div>
<div class="abs contact-btn contact-phone">
  <svg width="40" height="40" viewBox="0 0 24 24" fill="#fff"><path d="M6.6 10.8a15 15 0 0 0 6.6 6.6l2.2-2.2a1 1 0 0 1 1-.25 11.4 11.4 0 0 0 3.6.57 1 1 0 0 1 1 1V20a1 1 0 0 1-1 1A17 17 0 0 1 3 4a1 1 0 0 1 1-1h3.5a1 1 0 0 1 1 1c0 1.25.2 2.45.57 3.57a1 1 0 0 1-.25 1z"/></svg>
  <span>TEL：000-000-0000</span>
</div>
<div class="abs contact-btn contact-mail">
  <svg width="48" height="36" viewBox="0 0 48 36" fill="none" stroke="#fff" stroke-width="3"><rect x="2" y="2" width="44" height="32"/><path d="M2 2l22 18L46 2"/></svg>
  <span>メールでのお問い合わせ</span>
</div>

<footer>
  <div class="abs footer-brand">株式会社〇〇運送</div>
  <div class="abs footer-address">〒000-0000<br>〇〇県〇〇市〇〇町0-0</div>
  <nav class="abs footer-nav">
    <span>ホーム</span><span>事業案内</span><span>環境品質方針</span><span>車両案内</span>
    <span>採用情報</span><span>会社案内</span><span>お問い合わせ</span>
  </nav>
  <div class="abs copyright">© 2021 株式会社〇〇運送</div>
</footer>

</body>
</html>
```